Wine Label for a White and a Red Wine from Italy

We have a very good idea of what we want with artwork. We need you to please design a 'template' with the text so we can change out the artwork from year to year. Samples are shown of what we are looking for. We are looking for options with the two basic designs. Brand name of wine is: Valora di Castegno. Both wines are in a light green Bordeaux-style bottle (note: we don't show a light green bottle in the mockup but please remember the bottle is light green). Artwork is provided. We'd like to see either the green or blue butterfly on the white wine, the red butterfly is for the red wine. Please base the design on the attached label from Brailey and/or the attached label from Chateau Mervanges.

Target Market(s)

Millennials, women

Requirements
Must have
• The artwork (butterflies) attached.
Nice to have
• Elegant, readable fonts. Please make the text so it can be changed by the printer. Please make it so the artwork can be changed too.

```html
<!DOCTYPE html>
<html lang="en">
<head>
<meta charset="utf-8">
<title>Valora di Castegno – Barrel Select Labels</title>
<link rel="stylesheet" href="https://fonts.googleapis.com/css2?family=EB+Garamond:ital,wght@0,400;1,400&family=Montserrat:wght@400;500&display=swap">
<style>
  :root {
    --page: #ffffff;
    --label: #ffffff;
    --ink: #111111;
    --rule: #8a8a6a;
    --shadow: rgba(0, 0, 0, 0.55);
    --green-deep: #2f4a1e;
    --green-fresh: #a8c85a;
    --cream: #f4efe6;
    --ochre: #f2a516;
    --ochre-light: #f7c24a;
    --wing-red: #b3301c;
  }
  * { margin: 0; padding: 0; box-sizing: border-box; }
  html, body {
    width: 1200px;
    height: 848px;
    overflow: hidden;
    background: var(--page);
  }
  .sheet {
    position: relative;
    width: 1200px;
    height: 848px;
  }
  .label {
    position: absolute;
    width: 374px;
    height: 338px;
    background: var(--label);
    box-shadow: 9px 9px 10px var(--shadow);
    overflow: hidden;
    color: var(--ink);
  }
  .label--white-top { left: 174px; top: 58px; }
  .label--red-top   { left: 657px; top: 58px; }
  .label--white-bottom { left: 174px; top: 450px; }
  .label--red-bottom   { left: 657px; top: 450px; }

  .artwork { position: absolute; }
  .artwork--bianco {
    left: 60px; top: 60px; width: 230px; height: 260px;
    background:
      radial-gradient(ellipse 38% 28% at 40% 58%, var(--green-deep) 0%, rgba(47,74,30,0.6) 55%, rgba(47,74,30,0) 100%),
      radial-gradient(ellipse 40% 30% at 62% 42%, var(--green-fresh) 0%, rgba(168,200,90,0.4) 60%, rgba(168,200,90,0) 100%),
      radial-gradient(ellipse 55% 50% at 50% 50%, var(--cream) 0%, rgba(244,239,230,0) 100%);
  }
  .artwork--rosso {
    left: 55px; top: 0; width: 270px; height: 338px;
    background:
      radial-gradient(ellipse 30% 18% at 42% 50%, var(--wing-red) 0%, rgba(179,48,28,0.7) 60%, rgba(179,48,28,0) 100%),
      radial-gradient(ellipse 60% 55% at 55% 45%, var(--ochre) 0%, var(--ochre-light) 60%, rgba(247,194,74,0) 100%);
  }

  .brand, .tag, .wine, .footer { position: absolute; left: 0; width: 100%; text-align: center; }
  .brand-name {
    position: absolute; left: 0; width: 100%; top: 14px;
    font-family: "EB Garamond", Georgia, serif;
    font-size: 50px; line-height: 56px; font-weight: 400;
  }
  .brand-name--caps { font-size: 44px; letter-spacing: 1px; top: 18px; }
  .brand-sub {
    position: absolute; left: 0; width: 100%; top: 68px;
    font-family: "EB Garamond", Georgia, serif;
    font-size: 25px; line-height: 30px;
  }
  .rule {
    position: absolute; left: 112px; width: 150px; height: 1px;
    background: var(--rule);
  }
  .rule--head { top: 107px; }
  .rule--wine { top: 263px; left: 140px; width: 94px; }
  .tag {
    top: 117px;
    font-family: "Montserrat", Arial, sans-serif;
    font-size: 12.5px; line-height: 16px; letter-spacing: 3.2px;
  }
  .wine-type {
    position: absolute; left: 0; width: 100%; top: 244px;
    font-family: "EB Garamond", Georgia, serif;
    font-size: 14px; line-height: 18px; letter-spacing: 0.5px;
  }
  .vintage {
    position: absolute; left: 0; width: 100%; top: 266px;
    font-family: "EB Garamond", Georgia, serif;
    font-size: 14px; line-height: 18px;
  }
  .credit {
    position: absolute; left: 0; width: 100%; top: 297px;
    font-family: "Montserrat", Arial, sans-serif;
    font-size: 7px; line-height: 9px; letter-spacing: 0.4px;
  }
  .origin {
    position: absolute; left: 0; width: 100%; top: 313px;
    font-family: "EB Garamond", Georgia, serif;
    font-style: italic; font-size: 10px; line-height: 12px; letter-spacing: 0.6px;
  }
</style>
</head>
<body>
<main class="sheet">

  <section class="label label--white-top">
    <div class="artwork artwork--bianco" role="img" aria-label="Painted green butterfly artwork"></div>
    <h1 class="brand-name">Valora</h1>
    <p class="brand-sub">di Castegno</p>
    <div class="rule rule--head"></div>
    <p class="tag">BARREL SELECT</p>
    <p class="wine-type">BIANCO</p>
    <div class="rule rule--wine"></div>
    <p class="vintage">2018</p>
    <p class="credit">ARTISANALLY CRAFTED BY CANTINA SETTE COLLI • SUSTAINABLY FRAMED</p>
    <p class="origin">Piemonte - Italy</p>
  </section>

  <section class="label label--red-top">
    <div class="artwork artwork--rosso" role="img" aria-label="Red butterfly on ochre paint strokes artwork"></div>
    <h1 class="brand-name">Valora</h1>
    <p class="brand-sub">di Castegno</p>
    <div class="rule rule--head"></div>
    <p class="tag">BARREL SELECT</p>
    <p class="wine-type">ROSSO</p>
    <div class="rule rule--wine"></div>
    <p class="vintage">2018</p>
    <p class="credit">ARTISANALLY CRAFTED BY CANTINA SETTE COLLI • SUSTAINABLY FRAMED</p>
    <p class="origin">Piemonte - Italy</p>
  </section>

  <section class="label label--white-bottom">
    <div class="artwork artwork--bianco" role="img" aria-label="Painted green butterfly artwork"></div>
    <h1 class="brand-name brand-name--caps">VALORA</h1>
    <p class="brand-sub">di Castegno</p>
    <div class="rule rule--head"></div>
    <p class="tag">BARREL SELECT</p>
    <p class="wine-type">BIANCO</p>
    <div class="rule rule--wine"></div>
    <p class="vintage">2018</p>
    <p class="credit">ARTISANALLY CRAFTED BY CANTINA SETTE COLLI • SUSTAINABLY FRAMED</p>
    <p class="origin">Piemonte - Italy</p>
  </section>

  <section class="label label--red-bottom">
    <div class="artwork artwork--rosso" role="img" aria-label="Red butterfly on ochre paint strokes artwork"></div>
    <h1 class="brand-name brand-name--caps">VALORA</h1>
    <p class="brand-sub">di Castegno</p>
    <div class="rule rule--head"></div>
    <p class="tag">BARREL SELECT</p>
    <p class="wine-type">ROSSO</p>
    <div class="rule rule--wine"></div>
    <p class="vintage">2018</p>
    <p class="credit">ARTISANALLY CRAFTED BY CANTINA SETTE COLLI • SUSTAINABLY FRAMED</p>
    <p class="origin">Piemonte - Italy</p>
  </section>

</main>
</body>
</html>
```